Silver Brook Decorators Banner

Create a banner that displays and reinforces Silver Brook Decorators’ brand identity while promoting our interior painting services. The banner will be displayed at indoor venues through the winter. The design should be clean, professional, and visually recognizable to both new and returning customers. See attached design brief & logo source files.

```html
<!DOCTYPE html>
<html lang="en">
<head>
<meta charset="UTF-8">
<title>Silver Brook Decorators – Interior Painting Banner</title>
<link href="https://fonts.googleapis.com/css2?family=Outfit:wght@300;400;700;800&display=swap" rel="stylesheet">
<style>
  :root {
    --page-bg: #e6e6e3;
    --banner-bg: #efefea;
    --brand-green: #5f8c3c;
    --field-green: #6a9a3f;
    --ink-dark: #1f201f;
    --outline-ink: #3a3b3a;
    --band-grey: #a7acad;
    --edge-white: #f6f6f2;
    --photo-light: #d8d6d0;
    --photo-mid: #8e8a82;
    --photo-dark: #3b3a38;
  }
  * { box-sizing: border-box; margin: 0; padding: 0; }
  html, body { width: 1200px; height: 1200px; overflow: hidden; }
  body {
    background: var(--page-bg);
    font-family: "Outfit", sans-serif;
    position: relative;
  }
  .banner {
    position: absolute;
    left: 40px;
    top: 388px;
    width: 1120px;
    height: 424px;
    background: var(--banner-bg);
    overflow: hidden;
  }
  .banner-art {
    position: absolute;
    inset: 0;
    width: 1120px;
    height: 424px;
  }
  .headline {
    position: absolute;
    left: 54px;
    top: 68px;
    line-height: 0.92;
  }
  .headline-solid {
    display: block;
    font-size: 112px;
    font-weight: 800;
    color: var(--brand-green);
    letter-spacing: 2px;
  }
  .headline-outline {
    display: block;
    font-size: 112px;
    font-weight: 400;
    color: transparent;
    -webkit-text-stroke: 2px var(--outline-ink);
    letter-spacing: 2px;
  }
  .service-line {
    position: absolute;
    left: 58px;
    top: 268px;
    font-size: 31px;
    font-weight: 400;
    color: var(--brand-green);
  }
  .cta-bar {
    position: absolute;
    left: 6px;
    top: 341px;
    width: 400px;
    height: 48px;
    background: var(--ink-dark);
    color: #ffffff;
    padding: 7px 0 0 50px;
    font-size: 14px;
    line-height: 1.25;
  }
  .cta-url { letter-spacing: 3px; }
  .brand-name {
    position: absolute;
    left: 420px;
    top: 62px;
    width: 178px;
    text-align: center;
    font-size: 25px;
    font-weight: 800;
    line-height: 1.05;
    color: var(--brand-green);
  }
</style>
</head>
<body>
  <section class="banner">
    <svg class="banner-art" viewBox="0 0 712 270" preserveAspectRatio="none" aria-hidden="false">
      <defs>
        <linearGradient id="photoTone" x1="0" y1="0" x2="1" y2="1">
          <stop offset="0" stop-color="var(--photo-light)"/>
          <stop offset="0.55" stop-color="var(--photo-mid)"/>
          <stop offset="1" stop-color="var(--photo-dark)"/>
        </linearGradient>
      </defs>
      <rect class="accent-field" x="533" y="0" width="179" height="270" fill="var(--field-green)"/>
      <polygon class="arrow-band" points="470,0 565,0 702,135 585,270 470,270"
               fill="var(--band-grey)" stroke="var(--edge-white)" stroke-width="3"/>
      <polygon class="service-photo" role="img"
               aria-label="Photo of a painter kneeling on a drop cloth, rolling blue paint onto a white wall beside a stepladder"
               points="208,270 478,0 545,0 680,135 560,270" fill="url(#photoTone)"/>
    </svg>

    <h1 class="headline">
      <span class="headline-solid">INTE</span>
      <span class="headline-outline">RIOR</span>
    </h1>
    <p class="service-line">Painting Services</p>

    <div class="brand-name">SILVER BROOK DECORATORS</div>

    <div class="cta-bar">
      <div>Book a Free Estimate at</div>
      <div class="cta-url">www.silverbrookdeco.com</div>
    </div>
  </section>
</body>
</html>
```